Mosque App design fresh look and feel

Need to create a mosque app which has half a couple of dozen pages, a login page will take you into the main information with about 6 categories, such as school, memberships, information, prayer times etc... we have 3 types of users... 1. User .. admin user 3. imam user

I have xd files available.
https://mocks.plarvio.com/view/e4f7a2d1-8b3c-4f6e-a9d2-71b5c3e8f046-2ac7/

Target Market(s)

Muslims

Font styles to use
Sans Serif

Requirements
Must have
• Great UI
Simple flow

```html
<!DOCTYPE html>
<html lang="en">
<head>
<meta charset="utf-8">
<title>Noorwell Mosque App – Screens</title>
<link href="https://fonts.googleapis.com/css2?family=Cormorant+Garamond:wght@600&family=Nunito+Sans:wght@300;400;600;700&display=swap" rel="stylesheet">
<style>
  :root{
    --canvas:#f2f4f7;
    --green-top:#7cc497;
    --green-mid:#5f8f6e;
    --green-deep:#3d5c48;
    --field:rgba(255,255,255,0.30);
    --field-line:rgba(255,255,255,0.45);
    --button:#6c9b4e;
    --button-dark:#35502c;
    --text:#ffffff;
    --text-soft:rgba(255,255,255,0.78);
    --time:rgba(255,255,255,0.28);
    --avatar:#8a6a52;
  }
  *{box-sizing:border-box;margin:0;padding:0}
  html,body{width:1200px;height:2291px;overflow:hidden;background:var(--canvas)}
  body{position:relative;font-family:"Nunito Sans",sans-serif;color:var(--text)}

  .screen{position:absolute;width:500px;height:1090px;border-radius:34px;overflow:hidden;
    box-shadow:0 24px 50px rgba(40,60,50,0.18)}
  .screen--welcome{left:70px;top:50px}
  .screen--register{left:630px;top:50px}
  .screen--donate{left:70px;top:1170px}
  .screen--signin{left:630px;top:1170px}

  .scene-photo{position:absolute;inset:0;
    background:linear-gradient(180deg,var(--green-top) 0%,#6aa980 35%,var(--green-mid) 62%,var(--green-deep) 100%)}
  .scene-photo--muted{
    background:linear-gradient(180deg,#66977a 0%,#57856a 40%,#4a735a 70%,var(--green-deep) 100%)}

  .el{position:absolute}
  .brand{left:0;width:100%;text-align:center;font-family:"Cormorant Garamond",serif;font-weight:600;font-size:56px;letter-spacing:2px;line-height:1}
  .brand-sub{left:0;width:100%;text-align:center;font-weight:700;font-size:17px;letter-spacing:1.5px;color:var(--text-soft)}
  .clock{left:0;width:100%;text-align:center;font-weight:300;font-size:56px;color:var(--time)}
  .donate-pill{background:var(--button-dark);border-radius:4px;display:flex;align-items:center;justify-content:center;font-size:27px;font-weight:400}

  .cta{background:var(--button);border-radius:4px;display:flex;align-items:center;justify-content:space-between;padding:0 22px 0 30px;font-weight:700;font-size:21px}
  .cta svg{width:30px;height:20px}
  .footnote{left:0;width:100%;text-align:center;font-size:15px;font-weight:600;color:var(--text-soft)}
  .footnote b{color:var(--text)}

  .page-title{left:62px;font-family:"Cormorant Garamond",serif;font-weight:600;font-size:56px;line-height:1;letter-spacing:1px;color:rgba(255,255,255,0.85)}
  .page-sub{left:62px;font-size:34px;font-weight:400;letter-spacing:1px;line-height:1}
  .avatar{width:60px;height:60px;border-radius:50%;background:var(--avatar);border:3px solid rgba(255,255,255,0.6)}

  .label{left:62px;font-size:15px;font-weight:600;color:var(--text-soft)}
  .field{background:var(--field);border-radius:4px;display:flex;align-items:center;justify-content:space-between;padding:0 18px;font-size:28px;font-weight:300}
  .field svg{width:14px;height:24px}
  .field--hint{font-size:17px;color:rgba(255,255,255,0.55)}

  .pay-card{border-radius:4px;display:flex;flex-direction:column;align-items:center;justify-content:flex-end;padding-bottom:16px;font-size:21px;font-weight:600}
  .pay-card--card{background:rgba(255,255,255,0.55);color:#7ba05e}
  .pay-card--quick{background:var(--button)}
  .pay-card--more{background:var(--button)}
  .pay-card .mark{width:80px;height:80px;margin-bottom:22px}
  .plus{width:66px;height:66px;border-radius:50%;background:var(--button);display:flex;align-items:center;justify-content:center}

  .prayer{width:140px;height:70px;border-radius:4px;background:rgba(140,190,110,0.55);padding:10px 12px;font-weight:600}
  .prayer .name{font-size:18px}
  .prayer .time{font-size:13px;margin-top:8px;color:var(--text-soft)}
  .forgot{position:absolute;right:14px;top:50%;transform:translateY(-50%);background:var(--button);border-radius:8px;font-size:11px;padding:2px 8px;color:var(--text)}
</style>
</head>
<body>

<!-- Welcome -->
<section class="screen screen--welcome" aria-label="Welcome screen">
  <div class="scene-photo" role="img" aria-label="Mosque with tall minarets and domes under a hazy green sky"></div>
  <div class="el brand" style="top:160px">NOORWELL</div>
  <div class="el brand-sub" style="top:222px">MOSQUE APP</div>
  <div class="el clock" style="top:270px">6:15 PM</div>
  <div class="el donate-pill" style="left:165px;top:420px;width:175px;height:50px">Donate</div>
  <div class="el cta" style="left:80px;top:920px;width:328px;height:62px">Get Started
    <svg viewBox="0 0 30 20" fill="none" stroke="#fff" stroke-width="2"><path d="M1 10h27M20 2l8 8-8 8"/></svg></div>
  <div class="el footnote" style="top:1025px">Already pray before <b>Log in</b></div>
</section>

<!-- Register child -->
<section class="screen screen--register" aria-label="Register your child screen">
  <div class="scene-photo scene-photo--muted" role="img" aria-label="Faded mosque silhouette in green haze"></div>
  <div class="el page-title" style="top:100px">REGISTER</div>
  <div class="el page-sub" style="top:160px">YOUR CHILD</div>
  <div class="el avatar" style="left:400px;top:108px" role="img" aria-label="User profile photo"></div>

  <div class="el label" style="top:340px">Number of Children</div>
  <div class="el field" style="left:62px;top:365px;width:188px;height:63px">4
    <svg viewBox="0 0 14 24" fill="none" stroke="#fff" stroke-width="1.6"><path d="M2 8l5-5 5 5M2 16l5 5 5-5"/></svg></div>
  <div class="el label" style="top:471px">Name of child</div>
  <div class="el field" style="left:62px;top:494px;width:378px;height:63px">Yusuf Haddad</div>
  <div class="el label" style="top:589px">Age</div>
  <div class="el label" style="left:280px;top:589px">Gender</div>
  <div class="el field" style="left:62px;top:613px;width:160px;height:61px"><span></span>
    <svg viewBox="0 0 14 24" fill="none" stroke="#fff" stroke-width="1.6"><path d="M2 8l5-5 5 5M2 16l5 5 5-5"/></svg></div>
  <div class="el field" style="left:280px;top:613px;width:160px;height:61px"><span></span>
    <svg viewBox="0 0 14 24" fill="none" stroke="#fff" stroke-width="1.6"><path d="M2 8l5-5 5 5M2 16l5 5 5-5"/></svg></div>
  <div class="el label" style="top:705px">Quran reading level</div>
  <div class="el field" style="left:62px;top:727px;width:378px;height:63px"></div>

  <div class="el cta" style="left:86px;top:922px;width:330px;height:62px">Next Child
    <svg viewBox="0 0 30 20" fill="none" stroke="#fff" stroke-width="2"><path d="M1 10h27M20 2l8 8-8 8"/></svg></div>
  <div class="el footnote" style="left:-44px;top:1025px">Resgister with NOORWELL</div>
</section>

<!-- Donate -->
<section class="screen screen--donate" aria-label="Donate screen">
  <div class="scene-photo scene-photo--muted" role="img" aria-label="Faded mosque silhouette in green haze"></div>
  <div class="el page-title" style="top:100px">DONATE</div>
  <div class="el page-sub" style="top:162px;font-size:30px">FIND THE PEACE</div>
  <div class="el avatar" style="left:404px;top:108px" role="img" aria-label="User profile photo"></div>

  <div class="el label" style="top:254px">List of campaaigns</div>
  <div class="el field" style="left:62px;top:280px;width:385px;height:62px"><span></span>
    <svg viewBox="0 0 14 24" fill="none" stroke="#fff" stroke-width="1.6"><path d="M2 8l5-5 5 5M2 16l5 5 5-5"/></svg></div>

  <div class="el label" style="top:420px">Payment methods</div>
  <div class="el plus" style="left:380px;top:394px">
    <svg width="24" height="24" viewBox="0 0 24 24" stroke="#fff" stroke-width="3"><path d="M12 3v18M3 12h18"/></svg></div>

  <div class="el pay-card pay-card--card" style="left:62px;top:500px;width:170px;height:186px">
    <svg class="mark" viewBox="0 0 80 80" fill="none" stroke="#7ba05e" stroke-width="3">
      <rect x="6" y="22" width="56" height="40" rx="3"/><path d="M6 34h56M14 50h14"/>
      <path d="M58 14l14 5v10c0 8-6 13-14 16-8-3-14-8-14-16V19z" fill="rgba(255,255,255,0.5)"/>
      <path d="M52 28l5 5 9-9"/></svg>
    Credit card</div>
  <div class="el pay-card pay-card--quick" style="left:263px;top:500px;width:167px;height:186px">
    <svg class="mark" viewBox="0 0 80 80" fill="none"><rect x="24" y="24" width="32" height="32" rx="4" stroke="#fff" stroke-width="3"/></svg>
    Quickpay</div>
  <div class="el pay-card pay-card--more" style="left:463px;top:500px;width:60px;height:186px"></div>

  <div class="el label" style="top:772px">Amount</div>
  <div class="el field" style="left:62px;top:795px;width:385px;height:63px"></div>

  <div class="el cta" style="left:88px;top:933px;width:328px;height:62px">Donate now
    <svg viewBox="0 0 30 20" fill="none" stroke="#fff" stroke-width="2"><path d="M1 10h27M20 2l8 8-8 8"/></svg></div>
  <div class="el footnote" style="left:-8px;top:1024px">All the donation will be record.</div>
</section>

<!-- Sign in -->
<section class="screen screen--signin" aria-label="Sign in screen">
  <div class="scene-photo" role="img" aria-label="Mosque with tall minarets and domes under a hazy green sky"></div>
  <div class="el brand" style="top:160px">NOORWELL</div>
  <div class="el brand-sub" style="top:222px">MOSQUE APP</div>
  <div class="el clock" style="top:270px">6:15 PM</div>
  <div class="el donate-pill" style="left:166px;top:379px;width:173px;height:50px">Donate</div>

  <div class="el prayer" style="left:20px;top:471px"><div class="name">FAJR</div><div class="time">5:45am -6:15am</div></div>
  <div class="el prayer" style="left:180px;top:471px"><div class="name">DHUHR</div><div class="time">5:45am -6:15am</div></div>
  <div class="el prayer" style="left:340px;top:471px"><div class="name">ASR</div><div class="time">5:45am -6:15am</div></div>
  <div class="el prayer" style="left:20px;top:572px"><div class="name">MAGHRIB</div><div class="time">5:45am -6:15am</div></div>
  <div class="el prayer" style="left:180px;top:572px"><div class="name">ISHA</div><div class="time">5:45am -6:15am</div></div>
  <div class="el prayer" style="left:340px;top:572px"><div class="name">JUMA</div><div class="time">5:45pm -6:15pm</div></div>

  <div class="el field field--hint" style="left:88px;top:718px;width:328px;height:62px;padding-left:26px">Your email</div>
  <div class="el field field--hint" style="left:88px;top:826px;width:328px;height:63px;padding-left:26px">Your password<span class="forgot">Forgot?</span></div>
  <div class="el cta" style="left:88px;top:916px;width:328px;height:63px">SIGN IN
    <svg viewBox="0 0 30 20" fill="none" stroke="#fff" stroke-width="2"><path d="M1 10h27M20 2l8 8-8 8"/></svg></div>
  <div class="el footnote" style="left:-40px;top:1010px">Resgister with NOORWELL</div>
</section>

</body>
</html>
```